Web Design Project

Need a web design to be built by in-house team of developers. I need the look and feel of the site done ready for the developers to take over.

The site is a crowd funding site like www.pledgeloft.example. Our site will have all the main functions provided for on this site.
We are not looking for sophisticated investors, instead we are looking for people with an interest in investing but that need a lot of help and support through the process.

I have already obtained the logo. I attach it here.

I also want to have a coming soon page designed. I have sketched out what i want here and am uploading it in excel. this is obviously very basic and not what i will want for the main site.

colours should be light and accessible: blues, greens, yellows.

Site is to be fun and accessible.

site will have a lot of communication based aspects needed.

I am looking for a long term relationship with a designer to do this and to do many more things. I will have a lot of banners and desgin work to do here, and am looking ONLY for someone that can work on an ongoing basis (not full time, but a few hours a week).

I am also after an animation - basic 2 minute intro - not full animation, part powerpoint and part animation. I have made a separate tender for this, please quote me on it. I want the same person doing them all preferably....
Updates

Hi all

I am impressed with some of these designs. I have uploaded the wireframe of the coming soon page. 

I prefer the designs so far that are utilizing our little icons etc. 

obviously i understand you havent got root access or anything yet so are struggling to put them in, but its worth a try, some of the designs are using them well. 

i like bright colours. 

i would also show me how you are going to design other aspects eg chat box, forum page etc. 

Industry/Entity Type

Communication

Requirements
Must have
• the site will have all the functions of www.pledgeloft.example and www.venturibay.example.

```html
<!DOCTYPE html>
<html lang="en">
<head>
<meta charset="utf-8">
<title>Fundora – Projects</title>
<link rel="stylesheet" href="https://fonts.googleapis.com/css2?family=Noto+Sans:wght@400;700&display=swap">
<style>
:root{
  --page-bg:#3a6590;
  --page-bg-dark:#2f5883;
  --sheet:#ffffff;
  --panel-blue-top:#0a78ad;
  --panel-blue-bottom:#0b537e;
  --panel-orange-top:#ffd27a;
  --panel-orange-bottom:#f39a06;
  --orange-edge:#e07d00;
  --tag-orange:#fdb43a;
  --link-yellow:#ffe94a;
  --ink:#4a4a4a;
  --ink-brown:#3d2400;
  --heading-blue:#2f5f8f;
  --rule-blue:#2a5a8a;
  --progress-bg:#e4e3e4;
  --bar-blue:#0594d0;
  --bar-blue-dark:#0a5a88;
  --accent-orange:#f6a100;
  --footer-link:#2c5c8c;
}
*{box-sizing:border-box;margin:0;padding:0}
html,body{width:1200px;height:900px;overflow:hidden}
body{
  font-family:"Noto Sans",Tahoma,Verdana,sans-serif;
  background:linear-gradient(to bottom,var(--page-bg) 0,var(--page-bg-dark) 828px,#fff 828px);
  position:relative;
}
.sheet{position:absolute;left:83px;top:0;width:1024px;height:828px;background:var(--sheet)}
.abs{position:absolute}

/* news panel */
.news-panel{left:103px;top:-10px;width:289px;height:444px;border-radius:0 0 4px 4px;
  background:linear-gradient(to bottom,var(--panel-blue-top),var(--panel-blue-bottom));}
.date-tag{position:absolute;left:17px;width:93px;height:22px;border-radius:2px;
  background:linear-gradient(to bottom,#ffd27a,var(--tag-orange));
  color:#4a2a00;font-size:12.5px;text-align:center;line-height:22px;border-bottom:2px solid #e08a00}
.news-headline{position:absolute;left:17px;width:255px;color:#fff;font-weight:700;font-size:13px;line-height:15px}
.news-body{position:absolute;left:17px;width:262px;color:#fff;font-size:12px;line-height:14.5px}
.more-link{position:absolute;display:flex;align-items:center;gap:7px;font-size:12.5px;color:var(--link-yellow)}
.more-link svg{width:12px;height:8px}
.news-rule{position:absolute;left:17px;width:256px;height:1px;background:#3f86b4}
.follow-btn{position:absolute;left:17px;top:387px;width:154px;height:46px;border-radius:4px;
  background:linear-gradient(to bottom,#ffd98a,#f5a516);border:1px solid #f0c060;
  color:#4a2a00;font-size:14px;font-weight:700;line-height:18px;padding:4px 8px}

/* about panel */
.about-panel{left:103px;top:445px;width:289px;height:193px;border-radius:4px;
  background:linear-gradient(to bottom,var(--panel-orange-top),var(--panel-orange-bottom) 85%,var(--orange-edge));
  color:var(--ink-brown)}
.about-title{position:absolute;left:17px;top:10px;font-size:18px;font-weight:700;color:#4a2a00}
.about-body{position:absolute;left:17px;top:42px;width:260px;font-size:12.5px;line-height:16px}
.about-panel .more-link{color:#3d2400}

/* project cards */
.project-photo{position:absolute;width:130px;height:130px;
  background:linear-gradient(135deg,#c9d6e6,#6f8fb8 55%,#d9dee6);border:1px solid #aab}
.project-text{position:absolute;width:160px;font-size:12.5px;line-height:14.5px;color:var(--ink)}
.project-caption{position:absolute;font-size:12.5px;color:var(--ink)}
.progress{position:absolute;width:302px;height:59px;border-radius:4px;background:var(--progress-bg)}
.progress-bar{position:absolute;left:12px;top:11px;width:276px;height:20px}
.progress-label{position:absolute;left:9px;top:35px;font-size:15px;color:#111}
.progress-label b{font-weight:400;color:var(--accent-orange)}
.section-rule{position:absolute;height:1px;background:var(--rule-blue)}
.section-title{position:absolute;font-size:17px;color:var(--heading-blue)}
.view-more{left:979px;top:562px;width:93px;height:25px;border-radius:2px;
  background:linear-gradient(to bottom,#ffd27a,#f7a20c);border-bottom:2px solid #e08a00;
  font-size:13px;font-weight:700;color:#222;text-align:center;line-height:23px}

/* footer */
.site-footer{position:absolute;left:83px;top:661px;width:1024px;height:167px;border-top:1px solid var(--rule-blue);
  background:linear-gradient(to bottom,#fff 0,#f4f4f6 20%,#cfd0d4 85%,#fff 100%)}
.footer-nav{position:absolute;left:21px;top:28px;font-size:12.5px;color:var(--footer-link);word-spacing:1px}
.footer-nav span{margin:0 8px}
.footer-note{position:absolute;left:21px;top:60px;width:640px;font-size:12.5px;line-height:16px;color:var(--footer-link)}
.footer-copy{position:absolute;left:21px;top:108px;font-size:12.5px;color:var(--footer-link)}
</style>
</head>
<body>
<div class="sheet"></div>

<aside class="abs news-panel">
  <div class="date-tag" style="top:7px">21.08.2011</div>
  <div class="news-headline" style="top:36px">Headline will go here. Headline will go here.</div>
  <div class="news-body" style="top:76px">Normal text will go here. Normal text will go here. Normal text will go here. Normal text will go here. Normal text will go here.</div>
  <div class="more-link" style="left:18px;top:127px"><svg viewBox="0 0 12 8"><path d="M0 2h6V0l6 4-6 4V6H0z" fill="#e0d040"/></svg>read more</div>
  <div class="news-rule" style="top:155px"></div>

  <div class="date-tag" style="top:174px">21.08.2011</div>
  <div class="news-headline" style="top:206px">Headline will go here. Headline will go here.</div>
  <div class="news-body" style="top:246px">Normal text will go here. Normal text will go here. Normal text will go here. Normal text will go here. Normal text will go here.</div>
  <div class="more-link" style="left:18px;top:297px"><svg viewBox="0 0 12 8"><path d="M0 2h6V0l6 4-6 4V6H0z" fill="#e0d040"/></svg>read more</div>
  <div class="news-rule" style="top:325px"></div>

  <div class="more-link" style="left:18px;top:337px"><svg viewBox="0 0 12 8"><path d="M0 2h6V0l6 4-6 4V6H0z" fill="#e0d040"/></svg>see more posts</div>
  <div class="more-link" style="left:222px;top:337px">RSS
    <svg viewBox="0 0 16 16" style="width:16px;height:16px"><rect width="16" height="16" rx="2" fill="#f08a12"/><circle cx="4" cy="12" r="1.8" fill="#fff"/><path d="M3 7a6 6 0 0 1 6 6M3 3a10 10 0 0 1 10 10" stroke="#fff" stroke-width="2" fill="none"/></svg>
  </div>
  <div class="follow-btn">Follow us on<br>Chirpline</div>
</aside>

<section class="abs about-panel">
  <h2 class="about-title">What is Fundora funding?</h2>
  <p class="about-body">Fundorafunding is the new way for a community of like minded people to network and pool their money and knowledge together. Fundora provides a platform for entrepreneurs of start-ups and established businesses to connect with potential investors.</p>
  <div class="more-link" style="left:18px;top:163px"><svg viewBox="0 0 12 8"><path d="M0 2h6V0l6 4-6 4V6H0z" fill="#8a6a20"/></svg>read more</div>
</section>

<!-- project row 1 -->
<div class="project-photo" style="left:411px;top:1px" role="img" aria-label="Collage of business people around a globe"></div>
<p class="project-text" style="left:554px;top:3px">Text will go here. Text will go here. Text will go here. Text will go here. Text will go here. Text will go here. Text will go here. Text will go here. Text will go here. Text will go here. Text will go here.  will go here.</p>
<p class="project-caption" style="left:414px;top:137px">Text will go here. Text will</p>
<div class="progress" style="left:411px;top:169px">
  <svg class="progress-bar" viewBox="0 0 276 20"><rect x="0" y="0" width="20" height="10" fill="#f6a100"/><rect x="0" y="10" width="20" height="10" fill="#fcd58a"/><rect x="20" y="0" width="256" height="10" fill="#0594d0"/><rect x="20" y="10" width="256" height="10" fill="#0a5a88"/></svg>
  <div class="progress-label"><b>10%</b> invested so far</div>
</div>

<div class="project-photo" style="left:761px;top:1px" role="img" aria-label="Collage of business people around a globe"></div>
<p class="project-text" style="left:904px;top:3px">Text will go here. Text will go here. Text will go here. Text will go here. Text will go here. Text will go here. Text will go here. Text will go here. Text will go here. Text will go here. Text will go here.  will go here.</p>
<p class="project-caption" style="left:764px;top:137px">Text will go here. Text will</p>
<div class="progress" style="left:761px;top:169px">
  <svg class="progress-bar" viewBox="0 0 276 20"><rect x="0" y="0" width="20" height="10" fill="#f6a100"/><rect x="0" y="10" width="20" height="10" fill="#fcd58a"/><rect x="20" y="0" width="256" height="10" fill="#0594d0"/><rect x="20" y="10" width="256" height="10" fill="#0a5a88"/></svg>
  <div class="progress-label"><b>10%</b> invested so far</div>
</div>

<div class="section-rule" style="left:411px;top:250px;width:303px"></div>
<div class="section-rule" style="left:761px;top:250px;width:303px"></div>

<!-- project row 2 -->
<h3 class="section-title" style="left:411px;top:268px">Real World Gallery</h3>
<div class="project-photo" style="left:411px;top:301px" role="img" aria-label="Collage of business people around a globe"></div>
<p class="project-text" style="left:554px;top:303px">Text will go here. Text will go here. Text will go here. Text will go here. Text will go here. Text will go here. Text will go here. Text will go here. Text will go here. Text will go here. Text will go here.  will go here.</p>
<p class="project-caption" style="left:414px;top:437px">Text will go here. Text will</p>
<div class="progress" style="left:411px;top:469px">
  <svg class="progress-bar" viewBox="0 0 276 20"><rect x="0" y="0" width="20" height="10" fill="#f6a100"/><rect x="0" y="10" width="20" height="10" fill="#fcd58a"/><rect x="20" y="0" width="256" height="10" fill="#0594d0"/><rect x="20" y="10" width="256" height="10" fill="#0a5a88"/></svg>
  <div class="progress-label"><b>10%</b> invested so far</div>
</div>

<h3 class="section-title" style="left:761px;top:268px">Real World Gallery</h3>
<div class="project-photo" style="left:761px;top:301px" role="img" aria-label="Collage of business people around a globe"></div>
<p class="project-text" style="left:904px;top:303px">Text will go here. Text will go here. Text will go here. Text will go here. Text will go here. Text will go here. Text will go here. Text will go here. Text will go here. Text will go here. Text will go here.  will go here.</p>
<p class="project-caption" style="left:764px;top:437px">Text will go here. Text will</p>
<div class="progress" style="left:761px;top:469px">
  <svg class="progress-bar" viewBox="0 0 276 20"><rect x="0" y="0" width="20" height="10" fill="#f6a100"/><rect x="0" y="10" width="20" height="10" fill="#fcd58a"/><rect x="20" y="0" width="256" height="10" fill="#0594d0"/><rect x="20" y="10" width="256" height="10" fill="#0a5a88"/></svg>
  <div class="progress-label"><b>10%</b> invested so far</div>
</div>

<div class="section-rule" style="left:411px;top:550px;width:653px"></div>
<div class="abs view-more">view more</div>

<footer class="site-footer">
  <nav class="footer-nav">Contact us<span>|</span>Terms of Use<span>|</span>Pivacy policy<span>|</span>Sitemap<span>|</span>FAQ<span>|</span>Partnership Opportunities<span>|</span>Press</nav>
  <p class="footer-note">This website has been approved as a financial promotion by Harwell Prior which is authorised and regulated by the Financial Standards Office.</p>
  <p class="footer-copy">Copyright 2011-2012&nbsp; Fundora Limited All right reserved.</p>
</footer>
</body>
</html>
```